Labels for probiotic care products as Body Cream, Shower gel, Hand soap, ....

We are a starting a business in Flanders Belgium. We are looking for a label for care products, based on probiotics or good bacterie. We are looking for a fresh design that attracts people who wants a good product, based on naturally components. The products make that the microflora of the skin becomes and remains natural. The label must we be adaptive on bottles of 15 cm height to 8 cm height and a width of 4,5 cm. The brand name is KOVA REMU (beautiful skin in Hawaiian) or maybe just KOVA.

Industry/Entity Type

Business

Colors

Designer to choose colors to be used in the design.

Requirements
Must have
• somewhere the text "Probiotic Skin Care"
• I also have to tell that the bottles are white.
Nice to have
• I uploaded the 9 existing labels, but I want a totally new one, because the labels of our cleaning products are the same. I also uploaded a mood bord of labels I like.

```html
<!DOCTYPE html>
<html lang="nl">
<head>
<meta charset="utf-8">
<title>KOVA REMU – Skin Repair label</title>
<link rel="stylesheet" href="https://fonts.googleapis.com/css2?family=Jost:wght@400&family=Oswald:wght@300;500&display=swap">
<style>
  :root {
    --paper: #ffffff;
    --stage: #f4f4f4;
    --grey-type: #7a7a7a;
    --lime: #9cb51f;
    --lime-dark: #8aa314;
    --olive-ink: #3d4a05;
    --dieline: #e0208c;
    --mark: #222222;
    --body-ink: #1e1e1e;
    --block-grey: #9a9a9a;
  }
  * { margin: 0; padding: 0; box-sizing: border-box; }
  html, body { width: 1200px; height: 999px; overflow: hidden; background: var(--stage); }
  .canvas { position: relative; width: 1200px; height: 999px; }

  .label {
    position: absolute; left: 395px; top: 48px;
    width: 410px; height: 902px;
    background: var(--paper);
    border: 1px solid #d6d6d6;
    overflow: hidden;
  }
  .pattern-top {
    position: absolute; left: 0; top: 44px; width: 100%; height: 158px;
    background: linear-gradient(180deg, #f1f1f1 0%, #e9e9e9 55%, #fafafa 100%);
  }
  .pattern-microbes {
    position: absolute; left: 0; top: 484px; width: 100%; height: 172px;
    background: linear-gradient(180deg, #fbfbfb 0%, #ededed 60%, #e4e4e4 100%);
  }
  .info-panel {
    position: absolute; left: 0; top: 656px; width: 100%; height: 246px;
    background: linear-gradient(90deg, #e6e6e6, #f0f0f0 50%, #e4e4e4);
  }
  .accent-square {
    position: absolute; left: 220px; top: 26px; width: 65px; height: 92px;
    background: var(--block-grey);
  }
  .brand-band {
    position: absolute; left: 0; top: 240px; width: 180px; height: 35px;
    background: linear-gradient(90deg, var(--lime-dark), #b5cc3a 40%, var(--lime) 70%, #a9c22a);
    display: flex; align-items: center; justify-content: flex-end; padding-right: 8px;
  }
  .brand-name {
    font-family: "Oswald", sans-serif; font-weight: 500; font-size: 19px;
    color: var(--olive-ink); letter-spacing: 0.5px;
  }
  .product-name {
    position: absolute; left: 288px; top: 122px;
    transform-origin: 0 0; transform: rotate(90deg);
    font-family: "Jost", sans-serif; font-weight: 400; font-size: 60px;
    line-height: 1; white-space: nowrap; color: var(--grey-type);
  }
  .tagline {
    position: absolute; left: 84px; top: 536px; width: 173px;
    border-top: 1px solid #9a9a9a; border-bottom: 1px solid #9a9a9a;
    padding: 3px 0 2px;
    font-family: "Jost", sans-serif; font-size: 20px; color: var(--grey-type);
    white-space: nowrap; letter-spacing: 0.3px;
  }
  .description {
    position: absolute; left: 114px; top: 676px; width: 176px;
    font-family: "Oswald", sans-serif; font-weight: 300; font-size: 11px;
    line-height: 14px; color: var(--body-ink); text-align: justify;
  }
  .print-guides { position: absolute; left: 0; top: 0; width: 100%; height: 100%; }
</style>
</head>
<body>
<main class="canvas">
  <section class="label">
    <div class="pattern-top" role="img" aria-label="Fine grey line pattern of geometric triangles"></div>
    <div class="pattern-microbes" role="img" aria-label="Light grey line pattern of friendly bacteria and microbes"></div>
    <div class="info-panel"></div>

    <svg class="print-guides" viewBox="0 0 466 1025" preserveAspectRatio="none">
      <path d="M 82,765 C 82,880 150,953 225,953 C 300,953 368,880 368,765"
            fill="none" stroke="var(--lime)" stroke-width="9"/>
      <path d="M 75,80 Q75,68 87,68 L 364,68 Q376,68 376,80 C 376,200 365,260 365,400 L 365,620 C 365,680 375,700 375,760 C 375,870 300,957 225,957 C 150,957 75,870 75,760 C 75,700 85,680 85,620 L 85,400 C 85,260 75,200 75,80 Z"
            fill="none" stroke="var(--dieline)" stroke-width="1.2"/>
      <g stroke="var(--mark)" stroke-width="1" fill="none">
        <line x1="75" y1="12" x2="75" y2="40"/><line x1="376" y1="12" x2="376" y2="40"/>
        <line x1="75" y1="985" x2="75" y2="1013"/><line x1="376" y1="985" x2="376" y2="1013"/>
        <line x1="18" y1="956" x2="46" y2="956"/><line x1="404" y1="956" x2="432" y2="956"/>
      </g>
      <g stroke="var(--mark)" stroke-width="1.2" fill="none">
        <g transform="translate(225,26)"><circle r="7"/><circle r="3.5" fill="var(--mark)"/><line x1="-11" y1="0" x2="11" y2="0"/><line x1="0" y1="-11" x2="0" y2="11"/></g>
        <g transform="translate(33,512)"><circle r="7"/><circle r="3.5" fill="var(--mark)"/><line x1="-11" y1="0" x2="11" y2="0"/><line x1="0" y1="-11" x2="0" y2="11"/></g>
        <g transform="translate(417,512)"><circle r="7"/><circle r="3.5" fill="var(--mark)"/><line x1="-11" y1="0" x2="11" y2="0"/><line x1="0" y1="-11" x2="0" y2="11"/></g>
        <g transform="translate(225,998)"><circle r="7"/><circle r="3.5" fill="var(--mark)"/><line x1="-11" y1="0" x2="11" y2="0"/><line x1="0" y1="-11" x2="0" y2="11"/></g>
      </g>
    </svg>

    <div class="accent-square"></div>
    <div class="brand-band"><span class="brand-name">KOVA REMU</span></div>
    <h1 class="product-name">Skin Repair</h1>
    <p class="tagline">Probiotic Skin Care</p>
    <p class="description">Een probiotische huidcrème, voor volwassenen en kinderen. Dagelijks gebruik vormt een beschermende goede huidflora en reinigt diep. Aanbrengen op een droge huid.</p>
  </section>
</main>
</body>
</html>
```